Road Construction Company needs business cards

We would like a new business card designed for our business.

We're a road construction company based in Qld, Australia.

Can the business card please have the following information on it.

Name: Brent Malvoy
Position: General Manager
Phone: 0471 592 304
Email: Brent.malvoy@quendix.com.au
Address: 87 Harrowgate Ave, Pindarra, QLD, 4000
Website: www.quendix.com.au

Visually we'd like the card to be professional and simple.

Attached is our logo.

Our website is www.quendix.com.au

Target Market(s)

Men aged 25-60

Contact Information for Business Card

As listed in project description

Font styles to use
Serif

Requirements
Must have
• Large logo on back of card

```html
<!DOCTYPE html>
<html lang="en">
<head>
<meta charset="UTF-8">
<title>Quendix Business Card</title>
<link rel="stylesheet" href="https://fonts.googleapis.com/css2?family=Montserrat:wght@400;500;700;800&display=swap">
<style>
  :root {
    --backdrop: #4a4a4a;
    --card: #ffffff;
    --navy-blue: #0b56a6;
    --sky-blue: #2c9ad8;
    --ink: #1b1b1b;
  }
  * { margin: 0; padding: 0; box-sizing: border-box; }
  html, body {
    width: 1200px;
    height: 900px;
    overflow: hidden;
    background: var(--backdrop);
    font-family: "Montserrat", sans-serif;
  }
  .card {
    position: absolute;
    width: 660px;
    height: 377px;
    background: var(--card);
    box-shadow: 0 12px 30px rgba(0,0,0,0.45);
  }
  .card-front { left: 150px; top: 50px; }
  .card-back { left: 390px; top: 470px; }

  .wordmark {
    color: var(--navy-blue);
    font-weight: 800;
    letter-spacing: 0.02em;
    line-height: 1;
  }
  .card-front .wordmark {
    position: absolute;
    left: 0; right: 0; top: 140px;
    text-align: center;
    font-size: 96px;
  }
  .card-back .wordmark {
    position: absolute;
    right: 40px; top: 38px;
    font-size: 46px;
  }

  .person {
    position: absolute;
    left: 40px; top: 120px;
  }
  .person-name {
    font-size: 26px;
    font-weight: 700;
    text-transform: uppercase;
    letter-spacing: 0.01em;
  }
  .first-name { color: var(--sky-blue); }
  .last-name { color: var(--navy-blue); }
  .person-role {
    font-size: 17px;
    color: var(--ink);
    margin-top: 4px;
  }

  .address {
    position: absolute;
    right: 40px; top: 130px;
    text-align: right;
    font-size: 16px;
    line-height: 1.35;
    color: var(--ink);
  }

  .contacts {
    position: absolute;
    left: 40px; bottom: 34px;
    list-style: none;
    font-size: 17px;
    color: var(--ink);
  }
  .contacts li {
    display: flex;
    align-items: center;
    gap: 12px;
    margin-top: 6px;
  }
  .contacts svg { width: 18px; height: 18px; flex: none; fill: var(--navy-blue); }
</style>
</head>
<body>

<section class="card card-front">
  <div class="wordmark">QUENDIX</div>
</section>

<section class="card card-back">
  <div class="wordmark">QUENDIX</div>

  <div class="person">
    <div class="person-name"><span class="first-name">Brent</span> <span class="last-name">Malvoy</span></div>
    <div class="person-role">General Manager</div>
  </div>

  <address class="address" style="font-style:normal">
    87 Harrowgate Ave<br>
    Pindarra, QLD, 4000
  </address>

  <ul class="contacts">
    <li>
      <svg viewBox="0 0 24 24" aria-hidden="true"><path d="M3 9c0-3 4-5 9-5s9 2 9 5v1h-5V8H8v2H3z M6 12h12l2 8H4z"/></svg>
      0471 592 304
    </li>
    <li>
      <svg viewBox="0 0 24 24" aria-hidden="true"><path d="M2 5h20v14H2z M3 6l9 7 9-7" stroke="#fff" stroke-width="1.5"/></svg>
      Brent.malvoy@quendix.com.au
    </li>
    <li>
      <svg viewBox="0 0 24 24" aria-hidden="true"><circle cx="12" cy="12" r="10"/><path d="M2 12h20M12 2c3 3 3 17 0 20M12 2c-3 3-3 17 0 20" stroke="#fff" stroke-width="1.2" fill="none"/></svg>
      www.quendix.com.au
    </li>
  </ul>
</section>

</body>
</html>
```